Etiketten für Olivenöl-Intensivcreme
Zielgruppe
Wir produzieren Bio-Food, u.a. Wein und Olivenöl. Jetzt soll eine Olivenöl-Intensivcreme im Bereich Kosmetik auf dem Markt platziert werden. Unsere Zielgruppe hat ein sehr breites Altersspektrum (jung bis alt), ist naturverbunden, tierlieb, gebildet, kritisch-reflektierend, weiß gute Qualität zu schätzen, ist überwiegend weiblich. Die Olivenöl-Intensivcreme hat eine sehr breite Verwendung und soll sich als 'Allzweckwaffe' in jedem Haushalt etablieren (Babyhaut-Pflege, Lippenpflege, Ganzkörperpflege, Hand-Schutzcreme etc.).
Aufgabenstellung
Die Creme soll heißen: Tavunel (es könnte z.B. der Buchstabe 'O' durch eine Olive ersetzt werden). Es gibt zwei Etikette (Deckeloberseite der Metalldose und auf dem Boden). Der Durchmesser der Etikette ist jeweils 5,5 cm. Die Deckelunterseite gilt reinen Pflichtangaben. Im Dateidownloadbereich sind die Textvorgaben für die Etikette. MUT zur Farbe! Wir sind NICHT brav und angepasst! Orange kann Akzente setzen bzw. für Aufmerksamkeit im Regal sorgen.

```html
<!DOCTYPE html>
<html lang="de">
<head>
<meta charset="utf-8">
<title>Tavunel – Etiketten Entwurf 1</title>
<link rel="stylesheet" href="https://fonts.googleapis.com/css2?family=Fira+Sans+Condensed:wght@400;500;700&family=Courier+Prime:wght@400;700&family=Questrial&display=swap">
<style>
  :root{
    --bg-light:#f6f6f6;
    --bg-dark:#c4c4c4;
    --ink:#2a2a22;
    --label-pale:#ebebb0;
    --label-lime:#e3e27a;
    --strip-lime:#dedd78;
    --gold-light:#cdbd62;
    --gold-dark:#5c5220;
    --orange:#f39314;
    --orange-text:#e08a1a;
    --amber:#c79a1e;
    --olive:#8a7d34;
    --olive-deep:#4a4518;
    --green:#9cbf2c;
    --leaf:#4d6a1c;
    --white:#ffffff;
  }
  html,body{margin:0;padding:0;}
  body{width:900px;height:1200px;overflow:hidden;}
  .sheet{
    position:relative;width:900px;height:1200px;overflow:hidden;
    background:linear-gradient(135deg,var(--bg-dark) 0%,var(--bg-light) 45%,var(--bg-light) 70%,var(--bg-dark) 100%);
    font-family:"Fira Sans Condensed",sans-serif;color:var(--ink);
  }
  .sheet-title{position:absolute;top:48px;left:0;width:900px;text-align:center;font-size:19px;margin:0;font-weight:400;letter-spacing:.5px;}
  .variant-title{position:absolute;top:76px;font-size:19px;margin:0;font-weight:400;}
  .variant-c{left:250px;}
  .variant-d{left:577px;}
  .label{position:absolute;width:292px;height:292px;}
  .lid-c{left:138px;top:190px;}
  .lid-d{left:469px;top:190px;}
  .base-c{left:138px;top:499px;}
  .base-d{left:469px;top:499px;}
  .label svg{width:292px;height:292px;display:block;overflow:visible;}
  .t{font-family:"Fira Sans Condensed",sans-serif;}
  .brand-name{font-family:"Fira Sans Condensed",sans-serif;font-weight:500;}
  .house{font-family:"Questrial",sans-serif;}
  .mono{font-family:"Courier Prime",monospace;}
  .fill-pale{fill:var(--label-pale);}
  .fill-lime{fill:var(--label-lime);}
  .fill-strip{fill:var(--strip-lime);}
  .fill-white{fill:var(--white);}
  .fill-orange{fill:var(--orange);}
  .fill-olive-deep{fill:var(--olive-deep);}
  .c-orange{fill:var(--orange-text);}
  .c-amber{fill:var(--amber);}
  .c-olive{fill:var(--olive);}
  .c-olive-deep{fill:var(--olive-deep);}
  .c-green{fill:var(--green);}
  .c-leaf{fill:var(--leaf);}
  .c-ink{fill:var(--ink);}
  .c-white{fill:var(--white);}
  .placeholder-art{fill:var(--amber);opacity:.35;}
  .placeholder-icon{fill:var(--leaf);opacity:.8;}
  .ghost-house{fill:var(--white);opacity:.18;}
</style>
</head>
<body>
<div class="sheet">
  <h1 class="sheet-title">ENTWURF 1</h1>
  <h2 class="variant-title variant-c">variante C</h2>
  <h2 class="variant-title variant-d">variante D</h2>

  <!-- Variante C – Deckeloberseite -->
  <div class="label lid-c">
    <svg viewBox="0 0 300 300">
      <defs>
        <linearGradient id="goldBandC1" x1="0" x2="1" y1="0" y2="0">
          <stop offset="0" stop-color="var(--gold-light)"/>
          <stop offset="1" stop-color="var(--gold-dark)"/>
        </linearGradient>
        <clipPath id="discC1"><circle cx="150" cy="150" r="148"/></clipPath>
        <path id="arcC1" d="M213 32 A134 134 0 0 1 196 276"/>
      </defs>
      <g clip-path="url(#discC1)">
        <rect x="0" y="0" width="300" height="300" class="fill-pale"/>
        <rect x="80" y="0" width="140" height="16" fill="url(#goldBandC1)"/>
        <rect x="0" y="16" width="300" height="4" class="fill-white"/>
        <rect x="0" y="270" width="300" height="4" class="fill-white"/>
        <rect x="86" y="274" width="128" height="30" fill="url(#goldBandC1)"/>
      </g>
      <circle cx="58" cy="100" r="26" class="fill-olive-deep"/>
      <text x="90" y="118" font-size="42" class="brand-name c-olive">Tavunel</text>
      <text x="136" y="60" font-size="16" class="t c-amber">Pflege- &amp;</text>
      <text x="136" y="78" font-size="16" class="t c-amber">Schutzcreme</text>
      <text font-size="11" class="mono c-leaf"><textPath href="#arcC1">Vegane Naturkosmetik aus Bio-Oliven</textPath></text>
      <text x="70" y="164" font-size="20" text-anchor="middle" class="t c-amber">OLIVENÖL-</text>
      <text x="70" y="186" font-size="20" text-anchor="middle" class="t c-orange">INTENSIV</text>
      <text x="70" y="208" font-size="20" text-anchor="middle" class="t c-amber">CREME</text>
      <rect x="124" y="162" width="44" height="60" rx="6" class="placeholder-art" role="img" aria-label="Linienzeichnung eines galoppierenden Pferdes"/>
      <text x="68" y="241" font-size="22" class="house c-orange">MERELO.HOF</text>
    </svg>
  </div>

  <!-- Variante D – Deckeloberseite -->
  <div class="label lid-d">
    <svg viewBox="0 0 300 300">
      <defs>
        <clipPath id="discD1"><circle cx="150" cy="150" r="148"/></clipPath>
      </defs>
      <g clip-path="url(#discD1)">
        <rect x="0" y="0" width="300" height="300" class="fill-lime"/>
        <path d="M76 34 A74 23 0 0 1 224 34 Z" class="fill-orange"/>
        <rect x="0" y="275" width="300" height="5" class="fill-white"/>
        <rect x="0" y="280" width="300" height="20" class="fill-white" opacity="0"/>
        <path d="M84 280 A66 20 0 0 0 216 280 Z" class="fill-orange"/>
      </g>
      <text x="140" y="61" font-size="20" class="t c-amber" letter-spacing=".8">OLIVENÖL-</text>
      <text x="140" y="80" font-size="20" class="t c-orange" letter-spacing=".8">INTENSIV</text>
      <text x="140" y="99" font-size="20" class="t c-amber" letter-spacing=".8">CREME</text>
      <circle cx="75" cy="118" r="36" class="fill-olive-deep"/>
      <text x="118" y="158" font-size="46" class="brand-name c-green">Tavunel</text>
      <text x="140" y="187" font-size="15" class="t c-ink">Pflege- und Schutzcreme</text>
      <rect x="128" y="196" width="42" height="52" rx="6" class="placeholder-art" role="img" aria-label="Linienzeichnung eines galoppierenden Pferdes"/>
      <text x="178" y="211" font-size="13.5" class="t c-orange">Vegane</text>
      <text x="178" y="226" font-size="13.5" class="t c-orange">Naturkosmetik</text>
      <text x="178" y="241" font-size="13.5" class="t c-orange">aus Bio-Oliven</text>
      <text x="76" y="270" font-size="24" class="house c-olive">MERELO.HOF</text>
    </svg>
  </div>

  <!-- Variante C – Dosenboden -->
  <div class="label base-c">
    <svg viewBox="0 0 300 300">
      <defs>
        <linearGradient id="goldBandC2" x1="0" x2="1" y1="0" y2="0">
          <stop offset="0" stop-color="var(--gold-light)"/>
          <stop offset="1" stop-color="var(--gold-dark)"/>
        </linearGradient>
        <clipPath id="discC2"><circle cx="150" cy="150" r="148"/></clipPath>
      </defs>
      <g clip-path="url(#discC2)">
        <rect x="0" y="0" width="300" height="300" class="fill-pale"/>
        <rect x="86" y="14" width="128" height="14" fill="url(#goldBandC2)"/>
        <rect x="0" y="272" width="300" height="4" class="fill-white"/>
        <rect x="80" y="276" width="140" height="24" fill="url(#goldBandC2)"/>
        <path d="M252 60 Q290 150 252 235 Z" class="fill-strip"/>
      </g>
      <text x="150" y="26" font-size="11" font-weight="700" text-anchor="middle" class="t c-white">150ml</text>
      <circle cx="148" cy="64" r="18" class="fill-olive-deep"/>
      <text x="170" y="80" font-size="26" class="brand-name c-olive">Tavunel</text>
      <rect x="28" y="68" width="62" height="84" rx="8" class="placeholder-art" role="img" aria-label="Linienzeichnung eines galoppierenden Pferdes"/>
      <text x="222" y="93" font-size="10.5" text-anchor="end" class="t c-orange">Wasserfreie Creme - unparfümiert</text>
      <g font-size="8.6" text-anchor="end" class="t c-olive-deep">
        <text x="222" y="106">Ingredients: Olea Europaea Friut Oil,</text>
        <text x="222" y="117">Hydrogenated Rapeseed Oil,</text>
        <text x="220" y="128">Tocopherol</text>
      </g>
      <text x="80" y="143" font-size="10.5" font-weight="700" class="t c-orange">ANWENDUNG:</text>
      <g font-size="9.2" text-anchor="end" class="t c-orange">
        <text x="222" y="156">Sparsam auf die trockene Haut auftragen</text>
        <text x="222" y="167">(die Creme ist sehr ergiebig!).</text>
        <text x="222" y="179">Die Einwirkzeit kann einige Minuten dauern.</text>
        <text x="222" y="190">Vorher kann es beim Berühren von Gegenständen</text>
        <text x="222" y="201">mit den gecremten Körperpartien zur</text>
        <text x="222" y="212">Fettübertragung kommen.</text>
      </g>
      <text transform="translate(239 190) rotate(-90)" font-size="9" class="t c-ink">Mindestens haltbar:</text>
      <text transform="translate(256 180) rotate(-90)" font-size="8.5" font-weight="700" class="mono c-ink">JANUAR 2021</text>
      <rect x="50" y="203" width="32" height="30" rx="5" class="placeholder-icon" role="img" aria-label="Recycling-Symbol"/>
      <g font-size="8.6" text-anchor="middle" class="t c-ink">
        <text x="150" y="243">MERELO.HOF - Dr. med. Miriam Bessel</text>
        <text x="150" y="255">Hafenweg 12, D - 24000 Musterstadt - www.merelo.example</text>
      </g>
      <text x="150" y="288" font-size="9" text-anchor="middle" class="t c-white">Made in Germany</text>
    </svg>
  </div>

  <!-- Variante D – Dosenboden -->
  <div class="label base-d">
    <svg viewBox="0 0 300 300">
      <defs>
        <clipPath id="discD2"><circle cx="150" cy="150" r="148"/></clipPath>
      </defs>
      <g clip-path="url(#discD2)">
        <rect x="0" y="0" width="300" height="300" class="fill-strip"/>
        <path d="M82 24 A68 18 0 0 1 218 24 Z" class="fill-orange"/>
        <rect x="0" y="275" width="300" height="4" class="fill-white"/>
        <path d="M82 279 A68 20 0 0 0 218 279 Z" class="fill-orange"/>
      </g>
      <text x="150" y="20" font-size="9" text-anchor="middle" class="t c-white">Made in Germany</text>
      <circle cx="70" cy="62" r="22" class="fill-olive-deep"/>
      <text x="94" y="80" font-size="21" class="brand-name c-olive">Tavunel</text>
      <text x="100" y="44" font-size="10.5" class="t c-ink">Wasserfreie, unparfümierte Creme</text>
      <text x="170" y="64" font-size="10.5" font-weight="700" class="t c-orange">ANWENDUNG:</text>
      <g font-size="8.8" class="t c-ink">
        <text x="170" y="82">Sparsam auf die trockene</text>
        <text x="170" y="93">Haut auftragen (die Creme</text>
        <text x="170" y="103">ist sehr ergiebig!). Die Einwirk-</text>
        <text x="170" y="114">zeit kann einige Minuten dauern.</text>
        <text x="170" y="124">Vorher kann es beim</text>
        <text x="176" y="135">Berühren von Gegenständen</text>
        <text x="188" y="145">mit den gecremten</text>
        <text x="188" y="156">Körperpartien zur Fettüber-</text>
        <text x="188" y="166">tragung kommen.</text>
      </g>
      <rect x="106" y="102" width="40" height="100" rx="8" class="placeholder-art" role="img" aria-label="Blasse Linienzeichnung eines galoppierenden Pferdes"/>
      <g font-size="8.8" text-anchor="end" class="t c-ink">
        <text x="100" y="147">MERELO.HOF</text>
        <text x="100" y="158">Dr. med. Miriam Bessel</text>
        <text x="100" y="170">Hafenweg 12</text>
        <text x="100" y="181">D - 24000 Musterstadt</text>
        <text x="100" y="192">www.merelo.example</text>
      </g>
      <path d="M188 176 H284 L278 200 H186 Z" fill="var(--label-pale)" opacity=".7"/>
      <text x="192" y="187" font-size="9" class="t c-green">Mindestens haltbar bis:</text>
      <text x="192" y="198" font-size="8.6" font-weight="700" class="mono c-ink">JANUAR 2021</text>
      <text x="150" y="230" font-size="34" text-anchor="middle" class="house ghost-house">MERELO.HOF</text>
      <rect x="70" y="235" width="30" height="28" rx="5" class="fill-white" opacity=".9" role="img" aria-label="Recycling-Symbol"/>
      <g font-size="8.8" class="t c-orange" opacity=".8">
        <text x="120" y="245">Ingredients: Olea Europaea Friut Oil,</text>
        <text x="120" y="256">Hydrogenated Rapeseed Oil,</text>
        <text x="120" y="267">Tocopherol</text>
      </g>
      <text x="140" y="292" font-size="11" font-weight="700" text-anchor="middle" class="t c-white">150ml</text>
    </svg>
  </div>
</div>
</body>
</html>
```